Real estate development company, seeking investors and joint venture partners to fund

i have attached a investor proposal document to attact joint venture money partners to invest in property development. the existing document i have attached need s to be polised to a professional standard and needs to be in word , so i can edit the content on ongoing basis i.e. numbers and photos etc . this document will be updated with new opportunites, propoerties, feasibility edited and emailed to potential investors. This document needs to be Red hot!! Company name Bright meadow collective. All tables, place holders for photos need to be provided so i can easily remove and paste new /updated photos.

Target Market(s)

investors , money partners property developers

Requirements
Must have
• Design to be in word document

Content should be modifyable by me as each project will have unique cost, sales etc

i want to be able to email to my clients

i may also print as required
Nice to have
• Feel free to modify table/images/look and feel

```html
<!DOCTYPE html>
<html lang="en">
<head>
<meta charset="utf-8">
<title>Investor Report – Bright meadow collective</title>
<link href="https://fonts.googleapis.com/css2?family=Open+Sans:wght@300;400;600;700;800&display=swap" rel="stylesheet">
<style>
:root{
  --navy:#1f3a6c;
  --navy-dark:#1a3160;
  --orange:#f7941d;
  --grey-band:#eeeeee;
  --row:#f1f2f4;
  --text:#333a45;
  --muted:#6b7280;
  --rule:#d7d9de;
}
*{box-sizing:border-box;margin:0;padding:0}
html,body{width:1200px;height:3575px;overflow:hidden}
body{background:var(--navy);font-family:'Open Sans',Arial,sans-serif;color:var(--text);position:relative}
.page{position:absolute;width:514px;height:665px;background:#fff;overflow:hidden}
.col-l{left:65px}.col-r{left:602px}
.r1{top:51px}.r2{top:745px}.r3{top:1443px}.r4{top:2143px}.r5{top:2841px}
.abs{position:absolute}

/* header */
.page-header{position:absolute;top:28px;left:38px;right:26px;height:16px;display:flex;align-items:center;font-size:6.5px;color:var(--text)}
.contact-item{display:flex;align-items:center;gap:3px;margin-right:8px}
.contact-icon{width:11px;height:11px;border-radius:50%;background:var(--orange);display:flex;align-items:center;justify-content:center}
.doc-tag{margin-left:auto;background:var(--navy);color:#fff;font-size:9px;padding:1px 10px;line-height:14px}

/* footer */
.page-footer{position:absolute;left:14px;right:30px;bottom:20px;height:14px;display:flex;align-items:center;gap:5px}
.brand-dot{width:10px;height:10px;border-radius:50%;background:var(--orange);flex:none}
.brand-mini{font-size:5.5px;font-weight:700;color:var(--navy);white-space:nowrap}
.footer-rule{flex:1;height:1px;background:var(--rule)}
.page-no{font-size:7px;color:var(--muted)}

/* section title */
.section-title{position:absolute;background:var(--navy);color:#fff;font-weight:400;font-size:22px;display:flex;align-items:center;padding-left:26px}
.sub-head{position:absolute;color:var(--orange);font-weight:600;font-size:15px}
.photo{position:absolute}
.lorem{position:absolute;font-size:7.6px;line-height:1.38;color:var(--muted)}
.lorem p{margin-bottom:8px}

/* cover */
.cover-brand{position:absolute;left:53px;top:90px;display:flex;align-items:center;gap:12px}
.cover-brand .mark{width:46px;height:46px;border-radius:50%;background:var(--orange)}
.cover-brand span{font-size:21px;font-weight:700;color:var(--navy);line-height:1.1}
.cover-title{position:absolute;left:53px;top:220px;font-size:42px;font-weight:800;color:var(--orange)}
.cover-sub{position:absolute;left:53px;top:282px;width:279px;height:31px;background:var(--navy);color:#fff;font-size:21px;display:flex;align-items:center;padding-left:22px}
.prep-band{position:absolute;left:0;top:404px;width:514px;height:132px;background:var(--grey-band)}
.prep{position:absolute;left:53px;top:428px;font-size:11px;color:var(--text)}
.prep .name{font-size:27px;color:var(--orange);font-weight:300;margin:4px 0 8px}
.cover-contact{position:absolute;left:53px;top:626px;display:flex;font-size:9px}

/* contents */
.toc{position:absolute;left:197px;top:306px;width:260px;font-size:8.6px}
.toc li{list-style:none;display:flex;height:22.7px;align-items:center}
.toc li span:first-child{flex:1}
.toc li span:last-child{width:20px}

/* proposal */
.kv{position:absolute;left:39px;top:478px;font-size:8.5px}
.kv div{display:flex;height:22.8px;align-items:center}
.kv b{font-weight:400;width:156px}

/* tables */
table{border-collapse:collapse;width:100%}
.ftable{position:absolute;font-size:4.8px;line-height:1}
.ftable th{background:var(--orange);color:#fff;font-weight:700;text-align:left;padding:2px 4px;height:14px}
.ftable td{padding:1px 10px;height:8.1px;border-bottom:1px solid #fff;background:var(--row);font-weight:600}
.ftable td.total{background:var(--orange);color:#fff}
.ctable{position:absolute;left:35px;top:146px;width:438px;font-size:7.5px;line-height:1;table-layout:fixed}
.ctable .banner{background:var(--orange);color:#fff;text-align:center;height:22px;font-size:8px}
.ctable .cols th{background:var(--navy);color:#fff;font-weight:400;text-align:left;padding-left:4px;height:22px}
.ctable td{height:23.5px;padding:0 0 0 4px;border-bottom:1px solid #fff;border-right:1px solid #fff;background:#fff}
.ctable tr:nth-child(odd) td{background:var(--row)}
.ctable td:last-child{text-align:right;padding-right:6px}
.ctable tr.foot td{background:var(--orange);color:#fff;height:20px}
.stable{position:absolute;left:52px;top:496px;width:410px;font-size:7px;line-height:1}
.stable th{background:var(--orange);color:#fff;font-weight:600;height:12px;text-align:right;padding-right:10px}
.stable td{height:12.3px;border-bottom:1px solid #e4e5e8;padding:0 4px}
.stable td:not(:first-child){text-align:right;padding-right:10px}

/* market stats */
.stat{position:absolute;background:var(--orange);color:#fff;text-align:center}
.stat small{display:block;font-size:7px;margin-top:16px;font-weight:600}
.stat strong{display:block;font-size:27px;font-weight:400;margin-top:14px}
</style>
</head>
<body>

<!-- 1 Cover -->
<section class="page col-l r1">
  <div class="cover-brand"><div class="mark"></div><span>Bright meadow<br>collective</span></div>
  <h1 class="cover-title">Investor Report</h1>
  <div class="cover-sub">Dual occ development</div>
  <div class="prep-band"></div>
  <div class="photo" role="img" aria-label="Hands holding a tablet showing financial charts" style="left:306px;top:404px;width:208px;height:132px;background:linear-gradient(135deg,#3d4a5c,#9aa8b8 55%,#e4e8ee)"></div>
  <div class="prep">Prepared By:<div class="name">Daniel Whitford</div>Bright meadow collective<br>ABN: XXXXXXXX</div>
  <div class="cover-contact">
    <div class="contact-item"><div class="contact-icon"><svg width="6" height="6" viewBox="0 0 10 10"><path d="M2 1l2 2-1 1.5a6 6 0 0 0 2.5 2.5L7 6l2 2-1.5 1.5C4 9 1 6 .5 2.5z" fill="#fff"/></svg></div>M | 0412-555-019</div>
    <div class="contact-item"><div class="contact-icon"><svg width="6" height="6" viewBox="0 0 10 10"><rect x="1" y="2" width="8" height="6" fill="#fff"/><path d="M1 2l4 3 4-3" stroke="#f7941d" fill="none"/></svg></div>E | info@brightmeadowcollective.com.au</div>
  </div>
</section>

<!-- 2 Intro -->
<section class="page col-r r1">
  <header class="page-header"><div class="contact-item"><div class="contact-icon"></div>M | 0412-555-019</div><div class="contact-item"><div class="contact-icon"></div>E | info@brightmeadowcollective.com.au</div><div class="doc-tag">Dual occ development</div></header>
  <div class="abs" style="left:141px;top:143px;width:121px;height:118px;background:var(--orange)"></div>
  <div class="photo" role="img" aria-label="City skyscrapers seen from above" style="left:0;top:160px;width:243px;height:394px;background:linear-gradient(180deg,#c9d3dc,#7d8a98 45%,#4a5563)"></div>
  <div class="lorem" style="left:265px;top:325px;width:220px">
    <p>Lorem ipsum dolor sit amet, consectetuer adipiscing elit, sed diam nonummy nibh euismod tincidunt ut laoreet dolore magna aliquam erat volutpat. Ut wisi enim ad minim veniam, quis nostrud exerci tation ullamcorper suscipit lobortis nisl ut aliquip ex ea commodo consequat.</p>
    <p>Duis autem vel eum iriure dolor in hendrerit in vulputate velit esse molestie consequat, vel illum dolore eu feugiat nulla facilisis at vero eros et accumsan et iusto odio dignissim qui blandit praesent luptatum zzril delenit augue duis dolore te feugait nulla facilisi.</p>
    <p>Duis autem vel eum iriure dolor in hendrerit in vulputate velit esse molestie consequat, vel illum dolore eu feugiat nulla facilisis at vero eros et accumsan et iusto odio dignissim qui blandit praesent luptatum zzril delenit.</p>
  </div>
  <footer class="page-footer"><div class="brand-dot"></div><div class="brand-mini">Bright meadow collective</div><div class="footer-rule"></div><div class="page-no">2</div></footer>
</section>

<!-- 3 Contents -->
<section class="page col-l r2">
  <header class="page-header"><div class="contact-item"><div class="contact-icon"></div>M | 0412-555-019</div><div class="contact-item"><div class="contact-icon"></div>E | info@brightmeadowcollective.com.au</div><div class="doc-tag">Dual occ development</div></header>
  <div class="photo" role="img" aria-label="Glass towers seen from street level against a bright sky" style="left:0;top:71px;width:487px;height:207px;background:linear-gradient(180deg,#e8eef4,#8aa0b8 60%,#4f6a3a)"></div>
  <div class="section-title" style="left:25px;top:308px;width:143px;height:55px">Contents</div>
  <ul class="toc">
    <li><span>PROPOSAL</span><span>| 4</span></li><li><span>LOCATION</span><span>| 4</span></li><li><span>PHOTOS</span><span>| 5</span></li><li><span>FINANCIAL FEASIBILITY</span><span>| 5</span></li><li><span>CASH FLOW ANALYSIS</span><span>| 6</span></li><li><span>CAPITAL REQUIREMENTS</span><span>| 7</span></li><li><span>SUBURB PROFILE</span><span>| 8</span></li><li><span>COMPARABLE SALES DATA</span><span>| 10</span></li><li><span>PLANNING INFORMATION</span><span>| 13</span></li><li><span>TESTIMONIALS</span><span>| 16</span></li><li><span>WHO ARE YOU?</span><span>| 16</span></li><li><span>CONTACT</span><span>| 20</span></li>
  </ul>
  <footer class="page-footer"><div class="brand-dot"></div><div class="brand-mini">Bright meadow collective</div><div class="footer-rule"></div><div class="page-no">2</div></footer>
</section>

<!-- 4 Proposal -->
<section class="page col-r r2">
  <header class="page-header"><div class="contact-item"><div class="contact-icon"></div>M | 0412-555-019</div><div class="contact-item"><div class="contact-icon"></div>E | info@brightmeadowcollective.com.au</div><div class="doc-tag">Dual occ development</div></header>
  <div class="section-title" style="left:39px;top:70px;width:155px;height:57px">Proposal</div>
  <div class="photo" role="img" aria-label="Hands typing on a laptop beside architectural plans" style="left:39px;top:137px;width:444px;height:214px;background:linear-gradient(135deg,#b9bec4,#e7e9ec 50%,#8d949c)"></div>
  <div class="abs" style="left:404px;top:376px;width:77px;height:244px;background:var(--orange)"></div>
  <div class="sub-head" style="left:39px;top:370px">Project Goal:</div>
  <p class="abs" style="left:39px;top:393px;width:355px;font-size:7.8px;line-height:1.35">Purchase an existing house on a block of land, obtain development approval to demolish existing house and build two townhouses (dual occupancy side by side)</p>
  <div class="sub-head" style="left:39px;top:444px">Project Outcomes:</div>
  <div class="kv">
    <div><b>Project Type:</b>2 Townhouse Development</div>
    <div><b>Total Project Costs:</b>$1,900,000</div>
    <div><b>Total Cash/Equity Required:</b>$627,991</div>
    <div><b>Indicative Project Net Profit:</b>$250,093</div>
    <div><b>Indicative Project Return:</b>40%</div>
  </div>
  <footer class="page-footer"><div class="brand-dot"></div><div class="brand-mini">Bright meadow collective</div><div class="footer-rule"></div><div class="page-no">2</div></footer>
</section>

<!-- 5 Location -->
<section class="page col-l r3">
  <header class="page-header"><div class="contact-item"><div class="contact-icon"></div>M | 0412-555-019</div><div class="contact-item"><div class="contact-icon"></div>E | info@brightmeadowcollective.com.au</div><div class="doc-tag">Dual occ development</div></header>
  <div class="section-title" style="left:33px;top:79px;width:215px;height:56px">Project Location</div>
  <div class="photo" role="img" aria-label="Street map of the suburb and surrounding bayside area" style="left:31px;top:146px;width:447px;height:215px;background:linear-gradient(90deg,#b6d3ec 0 18%,#eceae4 18%)"></div>
  <div class="sub-head" style="left:35px;top:385px">OVERVIEW</div>
  <div class="abs" style="left:35px;top:413px;width:136px;height:100px;background:var(--navy);color:#fff;font-size:8.5px;font-weight:700;padding:12px 9px;line-height:2.6">Station : 1.4 KM<br>Freeway Access: 1.5 KM<br>Shopping Centre: 1 KM</div>
  <div class="photo" role="img" aria-label="Freeway running past trees" style="left:35px;top:513px;width:136px;height:92px;background:linear-gradient(180deg,#9fb7cf,#6f8a52 55%,#7c7f84)"></div>
  <div class="abs" style="left:205px;top:410px;width:230px">
    <div style="font-size:12px;font-weight:700;color:var(--navy);line-height:1.25">Include a brief description of the suburb.</div>
    <p style="font-size:8px;line-height:2.8;margin-top:4px">Leafy and chosen as most livable suburb in Melbourne on many occasions. Has good mix of primary and secondary schools. Family friendly with growing demographic</p>
  </div>
  <footer class="page-footer"><div class="brand-dot"></div><div class="brand-mini">Bright meadow collective</div><div class="footer-rule"></div><div class="page-no">2</div></footer>
</section>

<!-- 6 Photos -->
<section class="page col-r r3">
  <header class="page-header"><div class="contact-item"><div class="contact-icon"></div>M | 0412-555-019</div><div class="contact-item"><div class="contact-icon"></div>E | info@brightmeadowcollective.com.au</div><div class="doc-tag">Dual occ development</div></header>
  <div class="section-title" style="left:33px;top:72px;width:132px;height:55px">Photos</div>
  <div class="photo" role="img" aria-label="Existing single-storey house before development" style="left:33px;top:146px;width:227px;height:135px;background:linear-gradient(180deg,#b8cde2,#c9c2b4 55%,#7b7d74)"></div>
  <div class="photo" role="img" aria-label="Completed pair of double-storey townhouses" style="left:272px;top:146px;width:212px;height:135px;background:linear-gradient(180deg,#5d7fb0,#3c4450 55%,#6b6a5f)"></div>
  <div class="abs" style="left:199px;top:287px;width:61px;height:18px;background:#c9cbcf;font-size:9px;font-weight:600;text-align:center;line-height:18px">BEFORE</div>
  <div class="abs" style="left:268px;top:287px;width:62px;height:18px;background:#c9cbcf;font-size:9px;font-weight:600;text-align:center;line-height:18px">AFTER</div>
  <div class="abs" style="left:33px;top:325px;font-size:12px;font-weight:700;color:var(--navy)">Location</div>
  <div class="photo" role="img" aria-label="Aerial view of the suburb with nearby hospital, shops and primary school marked" style="left:33px;top:349px;width:451px;height:258px;background:linear-gradient(135deg,#8d8572,#a79d88 50%,#6e6b5c)"></div>
  <footer class="page-footer"><div class="brand-dot"></div><div class="brand-mini">Bright meadow collective</div><div class="footer-rule"></div><div class="page-no">2</div></footer>
</section>

<!-- 7 Feasibility -->
<section class="page col-l r4">
  <header class="page-header"><div class="contact-item"><div class="contact-icon"></div>M | 0412-555-019</div><div class="contact-item"><div class="contact-icon"></div>E | info@brightmeadowcollective.com.au</div><div class="doc-tag">Dual occ development</div></header>
  <div class="section-title" style="left:36px;top:76px;width:226px;height:55px">Feasibility Report</div>
  <div class="sub-head" style="left:39px;top:148px">Acquisition and Build Costs</div>
  <table class="ftable" style="left:39px;top:176px;width:433px">
    <tr><th style="background:#fff;width:155px"></th><th style="width:190px">Amount</th><th>Finance</th></tr>
    <tr><td>Land Purchase</td><td>$800,000</td><td>80% Residential</td></tr>
    <tr><td>Legal Fees</td><td>$3,000</td><td></td></tr>
    <tr><td>Stamp Duty</td><td>$53,400</td><td></td></tr>
    <tr><td>Development contributions</td><td>0</td><td></td></tr>
    <tr><td>Council, Water Rates</td><td>$3,000</td><td></td></tr>
    <tr><td>Loan Fees</td><td>$2,500</td><td></td></tr>
    <tr><td>Contingency 5%</td><td>$53,400</td><td></td></tr>
    <tr><td>Build Cost</td><td>$1,000,000</td><td></td></tr>
    <tr><td>Title &amp; Subdivision</td><td>$3,000</td><td></td></tr>
    <tr><td>Sales- Legal, Agency Cost</td><td>$40,000</td><td></td></tr>
    <tr><td>GST</td><td>$50,000</td><td></td></tr>
    <tr><td>Holding Cost</td><td>$70,000</td><td></td></tr>
    <tr><td class="total">TOTAL COST OF PROJECT</td><td style="background:#fff">2,163,300</td><td style="background:#fff"></td></tr>
  </table>
  <div class="sub-head" style="left:39px;top:392px">Sales Income</div>
  <table class="ftable" style="left:39px;top:419px;width:203px">
    <tr><th style="background:#fff"></th><th>Amount</th></tr>
    <tr><td style="height:24px">Total sales of 2 unit</td><td>$2,400,000</td></tr>
    <tr><td style="height:24px">Other income, rental</td><td>0</td></tr>
  </table>
  <div class="sub-head" style="left:37px;top:514px">Costs Summary</div>
  <table class="ftable" style="left:39px;top:540px;width:203px">
    <tr><th style="background:#fff"></th><th>Amount</th></tr>
    <tr><td style="height:17px">Total costs</td><td></td></tr>
    <tr><td style="height:17px">Total Bank Finance</td><td></td></tr>
  </table>
  <div class="sub-head" style="left:262px;top:514px">Project Performance</div>
  <table class="ftable" style="left:263px;top:540px;width:203px">
    <tr><th style="background:#fff"></th><th>Amount</th></tr>
    <tr><td style="height:17px">Net Profit</td><td>$236,000</td></tr>
    <tr><td style="height:17px">Other income, rental</td><td></td></tr>
  </table>
  <footer class="page-footer"><div class="brand-dot"></div><div class="brand-mini">Bright meadow collective</div><div class="footer-rule"></div><div class="page-no">2</div></footer>
</section>

<!-- 8 Capital requirements -->
<section class="page col-r r4">
  <header class="page-header"><div class="contact-item"><div class="contact-icon"></div>M | 0412-555-019</div><div class="contact-item"><div class="contact-icon"></div>E | info@brightmeadowcollective.com.au</div><div class="doc-tag">Dual occ development</div></header>
  <div class="section-title" style="left:35px;top:76px;width:277px;height:55px">Capital Requirements</div>
  <table class="ctable">
    <tr><th class="banner" colspan="3" style="font-weight:400">CAPITAL REQUIRED - TIME LINE</th></tr>
    <tr class="cols"><th style="width:142px">Month</th><th style="width:162px">Description/Stage</th><th>Amount</th></tr>
    <tr><td>April '16</td><td></td><td>$</td></tr><tr><td>May '16</td><td></td><td>$</td></tr><tr><td>June '16</td><td></td><td>$</td></tr><tr><td>July '16</td><td></td><td>$</td></tr><tr><td>August '16</td><td></td><td>$</td></tr><tr><td>September '16</td><td></td><td>$</td></tr><tr><td>October '16</td><td></td><td>$</td></tr><tr><td>November '16</td><td></td><td>$</td></tr><tr><td>December '16</td><td></td><td>$</td></tr><tr><td>January '17</td><td></td><td>$</td></tr><tr><td>February '17</td><td></td><td>$</td></tr><tr><td>March '17</td><td></td><td>$</td></tr><tr><td>April '17</td><td></td><td>$</td></tr><tr><td>May '17</td><td></td><td>$</td></tr><tr><td>June '17</td><td></td><td>$</td></tr><tr><td>July '17</td><td></td><td>$</td></tr>
    <tr class="foot"><td colspan="2">TOTAL CASH REQUIRED</td><td>$240,072.00</td></tr>
  </table>
  <footer class="page-footer"><div class="brand-dot"></div><div class="brand-mini">Bright meadow collective</div><div class="footer-rule"></div><div class="page-no">2</div></footer>
</section>

<!-- 9 Suburb profile -->
<section class="page col-l r5">
  <header class="page-header"><div class="contact-item"><div class="contact-icon"></div>M | 0412-555-019</div><div class="contact-item"><div class="contact-icon"></div>E | info@brightmeadowcollective.com.au</div><div class="doc-tag">Dual occ development</div></header>
  <div class="section-title" style="left:31px;top:78px;width:202px;height:57px">Suburb Profile</div>
  <div class="lorem" style="left:31px;top:149px;width:450px">
    <p>Lorem ipsum dolor sit amet, consectetuer adipiscing elit, sed diam nonummy nibh euismod tincidunt ut laoreet dolore magna aliquam erat volutpat. Ut wisi enim ad minim veniam, quis nostrud exerci tation ullamcorper suscipit lobortis nisl ut aliquip ex ea commodo consequat. Duis autem vel eum iriure dolor in hendrerit in vulputate velit esse molestie consequat, vel illum dolore eu feugiat nulla facilisis at vero eros et accumsan et iusto odio dignissim qui blandit praesent luptatum zzril delenit augue duis dolore te feugait nulla facilisi.</p>
    <p>Lorem ipsum dolor sit amet, cons ectetuer adipiscing elit, sed diam nonummy nibh euismod tincidunt ut laoreet dolore magna aliquam erat volutpat. Ut wisi enim ad minim veniam, quis nostrud exerci tation ullamcorper suscipit lobortis nisl ut aliquip ex ea commodo consequat.</p>
  </div>
  <svg class="abs" style="left:28px;top:290px" width="460" height="190" viewBox="0 0 460 190" font-family="Open Sans, sans-serif" font-size="6" fill="#555">
    <rect x="30" y="3" width="5" height="5" fill="#3b78c3"/><text x="38" y="8">House</text>
    <rect x="58" y="3" width="5" height="5" fill="#f7941d"/><text x="66" y="8">Unit</text>
    <text x="2" y="20">$10,000</text><text x="2" y="50">$8,000</text><text x="2" y="80">$6,000</text><text x="2" y="110">$4,000</text><text x="2" y="140">$0,000</text>
    <g stroke="#e5e6e9"><line x1="35" y1="18" x2="170" y2="18"/><line x1="35" y1="48" x2="170" y2="48"/><line x1="35" y1="78" x2="170" y2="78"/><line x1="35" y1="108" x2="170" y2="108"/><line x1="35" y1="138" x2="170" y2="138"/></g>
    <polyline fill="none" stroke="#3b78c3" stroke-width="1.2" points="35,75 45,73 55,72 65,70 75,71 85,68 95,67 105,66 115,65 125,63 135,60 145,55 155,48 160,40 170,32"/>
    <polyline fill="none" stroke="#f7941d" stroke-width="1.2" points="35,118 45,115 55,117 65,112 75,114 85,110 95,111 105,106 115,108 125,104 135,102 145,98 155,100 165,95 170,97"/>
    <rect x="178" y="32" width="14" height="3" fill="#3b78c3"/><rect x="178" y="42" width="14" height="3" fill="#f7941d"/>
    <g font-size="5.5"><text x="40" y="150" transform="rotate(-30 40 150)">Jul 2012</text><text x="80" y="150" transform="rotate(-30 80 150)">Jul 2014</text><text x="120" y="150" transform="rotate(-30 120 150)">Jul 2015</text><text x="160" y="150" transform="rotate(-30 160 150)">Jul 2016</text></g>
    <text x="80" y="175" font-size="7.5" font-weight="700">Median price</text>
    <text x="322" y="8" font-size="5.5">Source: Parkline Property Data</text>
    <rect x="440" y="20" width="9" height="4" fill="#3b78c3"/><rect x="440" y="28" width="9" height="4" fill="#f7941d"/>
    <text x="215" y="22">400</text><text x="215" y="52">300</text><text x="215" y="82">200</text><text x="215" y="112">100</text><text x="222" y="140">0</text>
    <g stroke="#e5e6e9"><line x1="230" y1="18" x2="430" y2="18"/><line x1="230" y1="48" x2="430" y2="48"/><line x1="230" y1="78" x2="430" y2="78"/><line x1="230" y1="108" x2="430" y2="108"/><line x1="230" y1="138" x2="430" y2="138"/></g>
    <g fill="#8fb2de">
      <rect x="240" y="110" width="2" height="28"/><rect x="250" y="95" width="2" height="43"/><rect x="260" y="60" width="2" height="78"/><rect x="270" y="55" width="2" height="83"/><rect x="280" y="70" width="2" height="68"/><rect x="290" y="50" width="2" height="88"/><rect x="300" y="62" width="2" height="76"/><rect x="310" y="48" width="2" height="90"/><rect x="320" y="58" width="2" height="80"/><rect x="330" y="52" width="2" height="86"/><rect x="340" y="60" width="2" height="78"/><rect x="350" y="45" width="2" height="93"/><rect x="360" y="55" width="2" height="83"/><rect x="370" y="48" width="2" height="90"/><rect x="380" y="62" width="2" height="76"/><rect x="390" y="50" width="2" height="88"/><rect x="400" y="42" width="2" height="96"/><rect x="410" y="58" width="2" height="80"/><rect x="420" y="65" width="2" height="73"/>
    </g>
    <g fill="#f7941d">
      <rect x="243" y="118" width="2" height="20"/><rect x="253" y="112" width="2" height="26"/><rect x="263" y="90" width="2" height="48"/><rect x="273" y="95" width="2" height="43"/><rect x="283" y="100" width="2" height="38"/><rect x="293" y="88" width="2" height="50"/><rect x="303" y="96" width="2" height="42"/><rect x="313" y="85" width="2" height="53"/><rect x="323" y="92" width="2" height="46"/><rect x="333" y="88" width="2" height="50"/><rect x="343" y="98" width="2" height="40"/><rect x="353" y="84" width="2" height="54"/><rect x="363" y="90" width="2" height="48"/><rect x="373" y="86" width="2" height="52"/><rect x="383" y="96" width="2" height="42"/><rect x="393" y="88" width="2" height="50"/><rect x="403" y="80" width="2" height="58"/><rect x="413" y="92" width="2" height="46"/><rect x="423" y="100" width="2" height="38"/>
    </g>
    <g font-size="5.5"><text x="235" y="150" transform="rotate(-30 235 150)">Jul 2012</text><text x="285" y="150" transform="rotate(-30 285 150)">Jul 2014</text><text x="335" y="150" transform="rotate(-30 335 150)">Jul 2015</text><text x="385" y="150" transform="rotate(-30 385 150)">Jul 2016</text></g>
    <text x="290" y="175" font-size="7.5" font-weight="700">Number of sales</text>
  </svg>
  <table class="stable">
    <tr><th style="background:var(--orange)"></th><th>HOUSE</th><th>UNIT</th></tr>
    <tr><td>Median price</td><td>$505,000</td><td>$372,500</td></tr>
    <tr><td>Quarterly growth</td><td>6.09%</td><td>-1.32%</td></tr>
    <tr><td>12-month growth</td><td>11.91%</td><td>6.43%</td></tr>
    <tr><td>Average Annual Growth</td><td>7.24%</td><td>5.27%</td></tr>
    <tr><td>Weekly median advertised rent</td><td>$360</td><td>$300</td></tr>
    <tr><td>Number of sales</td><td>260</td><td>179</td></tr>
    <tr><td>Gross rental yield</td><td>3.71%</td><td>4.19%</td></tr>
    <tr><td>Day on market</td><td>38.34</td><td>56.19</td></tr>
  </table>
  <footer class="page-footer"><div class="brand-dot"></div><div class="brand-mini">Bright meadow collective</div><div class="footer-rule"></div><div class="page-no">2</div></footer>
</section>

<!-- 10 Market data -->
<section class="page col-r r5">
  <header class="page-header"><div class="contact-item"><div class="contact-icon"></div>M | 0412-555-019</div><div class="contact-item"><div class="contact-icon"></div>E | info@brightmeadowcollective.com.au</div><div class="doc-tag">Dual occ development</div></header>
  <div class="section-title" style="left:33px;top:78px;width:178px;height:57px">Market Data</div>
  <div class="lorem" style="left:33px;top:148px;width:450px">
    <p>Lorem ipsum dolor sit amet, consectetuer adipiscing elit, sed diam nonummy nibh euismod tincidunt ut laoreet dolore magna aliquam erat volutpat. Ut wisi enim ad minim veniam, quis nostrud exerci tation ullamcorper suscipit lobortis nisl ut aliquip ex ea commodo consequat. Duis autem vel eum iriure dolor in hendrerit in vulputate velit esse molestie consequat, vel illum dolore eu feugiat nulla facilisis at vero eros et accumsan et iusto odio dignissim qui blandit praesent luptatum zzril delenit augue duis dolore te feugait nulla facilisi.</p>
    <p>Lorem ipsum dolor sit amet, cons ectetuer adipiscing elit, sed diam nonummy nibh euismod tincidunt ut laoreet dolore magna aliquam erat volutpat. Ut wisi enim ad minim veniam, quis nostrud exerci tation ullamcorper suscipit lobortis nisl ut aliquip ex ea commodo consequat.</p>
  </div>
  <div class="photo" role="img" aria-label="City skyline of high-rise towers" style="left:32px;top:274px;width:452px;height:340px;background:linear-gradient(180deg,#dfe6ee,#8b99a9 50%,#55606d)"></div>
  <div class="stat" style="left:92px;top:295px;width:97px;height:118px"><small>MEDIAN HOUSE</small><strong>$505K</strong></div>
  <div class="stat" style="left:203px;top:295px;width:97px;height:118px"><small>AUCTION CLEARENCE</small><strong>75%</strong></div>
  <div class="stat" style="left:92px;top:419px;width:97px;height:111px"><small>DAYS ON MARKET</small><strong>38</strong></div>
  <div class="stat" style="left:203px;top:419px;width:97px;height:111px"><small>SOLD THIS YEAR</small><strong>260</strong></div>
  <footer class="page-footer"><div class="brand-dot"></div><div class="brand-mini">Bright meadow collective</div><div class="footer-rule"></div><div class="page-no">2</div></footer>
</section>

</body>
</html>
```